Business Card Design Project

Need a business card designed for a horse racing/gambling centered company.
Company name is BrightQuill.com.au
Company colours are similar to those in the logo.
Something clean and modern , designer given liberty to be creative.
Incorporate the logo is preferred.
Single or Double Sided fine
Must include :
Name
Mobile Number
Email Address
Reason: Apologies, I have been traveling unexpectedly with business and just need the extra two days to reply and give feedback before making a decision.
Industry/Entity Type
Business

```html
<!DOCTYPE html>
<html lang="en">
<head>
<meta charset="utf-8">
<title>BrightQuill.com.au — Business Card, Front and Back</title>
<link rel="stylesheet" href="https://fonts.googleapis.com/css2?family=Tinos:wght@400&display=swap">
<style>
  :root {
    --page-bg: #ffffff;
    --ink: #111111;
    --card-white: #ffffff;
    --brand-teal: #00897f;
    --teal-deep: #007a72;
    --card-black: #000000;
    --text-light: #f4f4f4;
    --shadow: rgba(0, 0, 0, 0.62);
  }
  * { margin: 0; padding: 0; box-sizing: border-box; }
  html, body {
    width: 1200px;
    height: 900px;
    overflow: hidden;
    background: var(--page-bg);
  }
  .sheet {
    position: relative;
    width: 1200px;
    height: 900px;
    font-family: "Tinos", "Times New Roman", serif;
    color: var(--ink);
  }
  .side-label {
    position: absolute;
    font-size: 26px;
    line-height: 1;
  }
  .side-label--front { left: 64px; top: 64px; }
  .side-label--back { left: 575px; top: 485px; }

  .card {
    position: absolute;
    width: 527px;
    height: 264px;
    box-shadow: 14px 16px 12px var(--shadow);
  }
  .card--front {
    left: 50px;
    top: 123px;
    background: var(--card-white);
  }
  .card--back {
    left: 575px;
    top: 543px;
    background: linear-gradient(to bottom,
      var(--brand-teal) 0%,
      var(--card-black) 45%,
      var(--card-black) 58%,
      var(--teal-deep) 100%);
    color: var(--text-light);
    text-align: center;
  }

  .brand-mark {
    position: absolute;
    left: 14px;
    top: 30px;
    display: flex;
    align-items: center;
    gap: 16px;
  }
  .brand-mark__disc { width: 136px; height: 136px; flex: none; }
  .brand-mark__name {
    font-size: 28px;
    color: var(--brand-teal);
    white-space: nowrap;
  }

  .holder-details {
    position: absolute;
    left: 276px;
    top: 134px;
    font-size: 27px;
    line-height: 34px;
  }

  .back-email {
    position: absolute;
    left: 0;
    right: 0;
    padding-left: 48px;
    top: 132px;
    font-size: 27px;
    line-height: 36px;
  }
  .back-invite {
    position: absolute;
    left: 0;
    right: 0;
    top: 232px;
    font-size: 21px;
    line-height: 24px;
    white-space: nowrap;
  }
</style>
</head>
<body>
  <main class="sheet">
    <p class="side-label side-label--front">Front</p>
    <section class="card card--front" aria-label="Card front">
      <div class="brand-mark">
        <svg class="brand-mark__disc" viewBox="0 0 136 136" aria-hidden="true">
          <circle cx="68" cy="68" r="68" fill="var(--brand-teal)"/>
        </svg>
        <span class="brand-mark__name">BrightQuill.com.au</span>
      </div>
      <p class="holder-details">Your Name:<br>Contact:<br>123456789</p>
    </section>

    <p class="side-label side-label--back">Back</p>
    <section class="card card--back" aria-label="Card back">
      <p class="back-email">Email Address:<br>hello@brightquill.com.au</p>
      <p class="back-invite">join us on http://www.brightquill.com.au/club</p>
    </section>
  </main>
</body>
</html>
```